Anzeigengestaltung für Fachzeitungen
Zielgruppe
Beratung von Managementsystem ISO 9001 (Qualität), ISO 14001 (Umwelt), ISO 50001 (Energie) für Firmen jeder Art
Aufgabenstellung
Es gibt ein Logo das auf Geschäftspapier verwendet wird. In der angehängten Datei ist eine bisher verwendete Anzeige eingestellt, an die für Informationen dient. In der Gestaltung sind Sie aber frei. Ziel der Anzeige ist Kundengewinnung im Bereich interne Audits, Beratung und Unterstützung, Schulung im Bereich von DIN EN ISO Normen 9001, 14001, 50001.
Die Anzeige wird in den VRT Zeitungen veröffentlicht und hat eine Größe von B90 H60

```html
<!DOCTYPE html>
<html lang="de">
<head>
<meta charset="utf-8">
<title>VERANOX – Anzeige Managementsysteme</title>
<link rel="stylesheet" href="https://fonts.googleapis.com/css2?family=Open+Sans:ital,wght@0,400;0,600;0,700;1,400&display=swap">
<style>
  :root {
    --page: #ffffff;
    --brand-green: #7aab21;
    --text-green: #6ea323;
    --navy: #053a6d;
    --white: #ffffff;
    --grass-dark: #2c5414;
    --grass-mid: #5a9428;
    --grass-light: #c4df9a;
  }
  * { box-sizing: border-box; margin: 0; padding: 0; }
  html, body {
    width: 1200px; height: 846px; overflow: hidden;
    background: var(--page);
    font-family: "Open Sans", Arial, sans-serif;
  }
  .ad {
    position: absolute; left: 86px; top: 80px;
    width: 1027px; height: 684px;
    background: var(--brand-green);
    box-shadow: 4px 5px 8px rgba(0,0,0,0.35);
    overflow: hidden;
  }
  .ad__visual {
    position: absolute; left: 0; top: 0; width: 1027px; height: 491px;
    background:
      radial-gradient(ellipse 420px 300px at 88% 25%, var(--grass-light) 0%, rgba(196,223,154,0) 100%),
      linear-gradient(90deg, var(--grass-dark) 0%, var(--grass-mid) 45%, #78ad3a 75%, var(--grass-mid) 100%);
  }
  .services {
    position: absolute; left: 43px; top: 0; width: 405px; height: 349px;
    background: var(--white);
    list-style: none;
    padding-top: 33px;
    color: var(--text-green);
    font-size: 26px; letter-spacing: 1.2px; line-height: 42.4px;
  }
  .services li { position: relative; padding-left: 72px; }
  .services .tick {
    position: absolute; left: 37px; top: 11px; width: 24px; height: 22px;
  }
  .services .norm { font-weight: 700; letter-spacing: 0.8px; }
  .transition {
    position: absolute; left: 0; top: 351px; width: 484px; height: 140px;
    background: var(--navy);
    color: var(--white);
    font-style: italic; font-size: 26px; line-height: 40px;
    padding: 10px 0 0 50px;
  }
  .brand-bar { position: absolute; left: 0; top: 491px; width: 1027px; height: 193px; color: var(--white); }
  .brand-name {
    position: absolute; left: 46px; top: 10px;
    font-size: 48px; font-weight: 700; letter-spacing: 0.5px;
  }
  .tagline {
    position: absolute; left: 385px; top: 22px;
    font-size: 32px; font-weight: 700;
  }
  .brand-rule { position: absolute; left: 46px; top: 72px; width: 946px; height: 2px; background: var(--white); }
  .credential { position: absolute; left: 46px; top: 80px; font-size: 23px; letter-spacing: 0.3px; }
  .contact { position: absolute; left: 46px; top: 137px; font-size: 24px; }
  .website { position: absolute; right: 35px; top: 130px; font-size: 31px; font-weight: 700; }
</style>
</head>
<body>
  <section class="ad">
    <div class="ad__visual" role="img" aria-label="Foto: zwei Hände halten eine Erdkugel vor grünem Grashintergrund"></div>

    <ul class="services">
      <li><svg class="tick" viewBox="0 0 24 22"><path d="M2 12 L9 20 L22 2" fill="none" stroke="currentColor" stroke-width="3" stroke-linecap="round" stroke-linejoin="round"/></svg>INTERNE AUDITS</li>
      <li><svg class="tick" viewBox="0 0 24 22"><path d="M2 12 L9 20 L22 2" fill="none" stroke="currentColor" stroke-width="3" stroke-linecap="round" stroke-linejoin="round"/></svg>BERATUNG</li>
      <li><svg class="tick" viewBox="0 0 24 22"><path d="M2 12 L9 20 L22 2" fill="none" stroke="currentColor" stroke-width="3" stroke-linecap="round" stroke-linejoin="round"/></svg>UNTERSTÜTZUNG</li>
      <li><svg class="tick" viewBox="0 0 24 22"><path d="M2 12 L9 20 L22 2" fill="none" stroke="currentColor" stroke-width="3" stroke-linecap="round" stroke-linejoin="round"/></svg>SCHULUNG IM</li>
      <li>BEREICH VON</li>
      <li class="norm">DIN EN ISO NORMEN</li>
      <li class="norm">9001, 14001, 50001</li>
    </ul>

    <div class="transition">
      <p>Umstellung leichtgemacht!</p>
      <p>ISO 9001:2015, ISO 14001:2015</p>
      <p>ISO 50001:2011</p>
    </div>

    <footer class="brand-bar">
      <div class="brand-name">VERANOX</div>
      <div class="tagline">Ihr Partner für Managementsysteme</div>
      <div class="brand-rule"></div>
      <p class="credential">Leadauditor verschiedener Zertifizierungsgesellschaften</p>
      <p class="contact">Mobil: 0170 1234567 | info@veranox.de</p>
      <p class="website">www.veranox.de</p>
    </footer>
  </section>
</body>
</html>
```